Redesign responsive website and logo for webshop platform

Redesign our applications old website with a new clean, crisp modern looking style that is responsive.

Our application is a cloud based, free ecommerce platform that lets users set up their own webshops within minutes. (Similar to Mabrook https://mabrook.example/l/sell)

Our old website: http://sv.vendlyx.example/

I need redesigned HTML + CSS for the following three pages:
* Landing Page:
(Old page: http://sv.vendlyx.example/)
I have attached a mockup of a proposed layout/structure for the landing page.
- Pricing comparision/features page
(Old page http://sv.vendlyx.example/t/funktioner)
- Generic "article" page:
(Old page http://sv.vendlyx.example/d/redigerasida)

The pages must responsive using HTML 5/CSS 3 (I prefer Bootstrap 3 if possible).

I also need a redesign of the logotype.

If you have any questions don't hesitate to ask and we will provide whatever is needed to you.

Logo Text

Vendlyx

Coding

Coded - Design and coding required

Number of Pages Required

3 page

Font styles to use
Serif
Sans Serif

```html
<!DOCTYPE html>
<html lang="sv">
<head>
<meta charset="utf-8">
<title>Vendlyx – Starta en gratis webshop</title>
<link rel="stylesheet" href="https://fonts.googleapis.com/css2?family=Raleway:wght@600;700;800&family=Cabin:wght@400;600;700&display=swap">
<style>
:root{
  --accent:#f2b705;
  --accent-dark:#e59a00;
  --ink:#111;
  --text:#333;
  --muted:#8fbcc6;
  --rule:#b9d5db;
  --hero-a:#a9cfd2;
  --hero-b:#8fb7bb;
  --band:#f3f3f3;
  --foot:#000;
}
*{box-sizing:border-box;margin:0;padding:0}
html,body{width:787px;height:1200px;overflow:hidden;background:#fff}
body{font-family:"Cabin",sans-serif;color:var(--text);position:relative}
a{text-decoration:none}
.hero{position:absolute;left:0;top:0;width:787px;height:430px}
.hero-photo{position:absolute;inset:0;
  background:linear-gradient(100deg,var(--hero-a) 0%,#9cc4c7 55%,#7a9aa3 75%,#c9ccc6 100%)}
.header{position:absolute;left:0;top:0;width:787px;height:36px;border-bottom:1px solid rgba(255,255,255,.5)}
.logo{position:absolute;left:95px;top:11px;font:700 16px "Raleway",sans-serif;color:#fff;letter-spacing:.3px}
.top-links{position:absolute;right:95px;top:14px;display:flex;gap:10px;font-size:7px;font-weight:600;color:#fff;align-items:center}
.top-links span{display:flex;align-items:center;gap:3px}
.top-links .login{color:var(--accent)}
.dot{width:5px;height:5px;border-radius:50%;background:currentColor;display:inline-block}
.hero-copy{position:absolute;left:95px;top:127px;width:360px;color:var(--ink)}
.hero-copy h1{font:800 19px "Raleway",sans-serif;letter-spacing:.1px}
.hero-copy p{font-size:11px;line-height:15.5px;margin-top:2px}
.btn{display:inline-flex;align-items:center;justify-content:center;border-radius:4px;font:700 9px "Cabin",sans-serif;text-transform:uppercase}
.btn-primary{background:var(--accent);color:#fff}
.hero .btn-primary{position:absolute;left:95px;top:209px;width:135px;height:31px}
.features-title{position:absolute;top:488px;width:787px;text-align:center;font:800 15px "Raleway",sans-serif;color:var(--accent)}
.features-title::after{content:"";display:block;width:30px;height:2px;background:var(--accent);margin:3px auto 0}
.feature{position:absolute;width:180px;text-align:center}
.feature svg{display:block;margin:0 auto 4px}
.feature h3{font:700 11px "Raleway",sans-serif;color:var(--ink)}
.feature p{font-size:7px;line-height:11px;margin-top:3px}
.spec-label{position:absolute;left:95px;font:800 8.5px "Raleway",sans-serif;color:var(--muted);text-transform:uppercase}
.spec{position:absolute;width:138px;border-top:1.5px solid var(--rule);border-bottom:1.5px solid var(--rule);height:78px;padding-top:6px}
.spec h4{font:700 9.5px "Cabin",sans-serif;color:var(--ink)}
.spec p{font-size:6.6px;line-height:10.5px}
.spec .more{color:var(--accent-dark);font-weight:700}
.arrow{position:absolute}
.cta-row{position:absolute;top:990px;left:259px;display:flex;gap:8px}
.cta-row .btn{height:31px}
.cta-row .btn-primary{width:136px}
.btn-outline{width:129px;border:1.5px solid var(--accent-dark);color:var(--accent-dark);text-transform:none;font-size:10px}
.contact-band{position:absolute;top:1101px;left:0;width:787px;height:34px;background:var(--band);display:flex;justify-content:space-around;align-items:center;padding:0 110px;font:700 8px "Cabin",sans-serif;color:var(--ink)}
.contact-band span{display:flex;align-items:center;gap:3px}
.ico{width:8px;height:7px;background:var(--accent);border-radius:1px;display:inline-block}
.footer{position:absolute;top:1135px;left:0;width:787px;height:65px;background:var(--foot);color:#bbb;font-size:6.5px;font-weight:700}
.footer nav{position:absolute;left:95px;top:29px}
.footer nav a{color:#bbb}
.footer nav i{font-style:normal;margin:0 6px}
.footer small{position:absolute;right:95px;top:29px;font-size:6.5px;font-weight:400;color:#999}
</style>
</head>
<body>
<section class="hero">
  <div class="hero-photo" role="img" aria-label="Foto: man i blå tröja sitter i en ljus soffa och arbetar på en bärbar dator"></div>
  <header class="header">
    <div class="logo">vendlyx</div>
    <div class="top-links">
      <span><i class="dot"></i>info@vendlyx.example</span>
      <span><i class="dot"></i>Vendlyx på Chirpnet</span>
      <span class="login"><i class="dot"></i>LOGGA IN</span>
    </div>
  </header>
  <div class="hero-copy">
    <h1>STARTA EN GRATIS WEBSHOP</h1>
    <p>Vendlyx är en tjänst som låter dig starta en komplett internetbutik. Tjänsten är gratis och har allt som krävs för att du ska komma igång med din verksamhet och sälja produkter online.</p>
  </div>
  <a class="btn btn-primary">&gt;&nbsp; Skapa en webshop</a>
</section>

<h2 class="features-title">FUNKTIONER</h2>

<div class="feature" style="left:99px;top:535px">
  <svg width="20" height="24" viewBox="0 0 20 24"><path d="M3 2h14M3 22h14M5 2c0 6 10 6 10 10S5 16 5 22M15 2c0 6-10 6-10 10s10 4 10 10" fill="none" stroke="#111" stroke-width="2"/><path d="M7 20l3-3 3 3z" fill="#111"/></svg>
  <h3>Kom igång på 5 minuter</h3>
  <p>Att starta en ebutik med Vendlyx tar inte mer än 5 minuter. Skapa ett konto för att komma igång. Ingenting behöver installeras på din dator.</p>
</div>
<div class="feature" style="left:304px;top:535px">
  <svg width="24" height="24" viewBox="0 0 24 24"><circle cx="12" cy="12" r="10" fill="none" stroke="#111" stroke-width="2"/><path d="M5 19L19 5" stroke="#111" stroke-width="2"/><text x="12" y="16" font-size="11" font-weight="700" text-anchor="middle" fill="#111">$</text></svg>
  <h3>Skapa en gratis webbutik</h3>
  <p>Vendlyx är en gratis tjänst. Tjänsten har varken månadskostnader eller transaktionsavgifter på det du säljer.</p>
</div>
<div class="feature" style="left:509px;top:535px">
  <svg width="24" height="24" viewBox="0 0 24 24"><circle cx="12" cy="11" r="5" fill="#111"/><rect x="10" y="16" width="4" height="5" fill="#111"/><path d="M12 1v3M3 5l2 2M21 5l-2 2M1 11h3M20 11h3" stroke="#111" stroke-width="1.5"/></svg>
  <h3>Intuitivt användargränssnitt</h3>
  <p>Det går snabb att lägga till nya produkter. Organisera produkter genom att dra och släppa.</p>
</div>
<div class="feature" style="left:99px;top:635px">
  <svg width="24" height="24" viewBox="0 0 24 24"><circle cx="10" cy="10" r="6" fill="none" stroke="#111" stroke-width="2.5"/><path d="M14 14l7 7" stroke="#111" stroke-width="3"/><circle cx="16" cy="5" r="3" fill="#111"/></svg>
  <h3>Sökmotoroptimerad</h3>
  <p>Vendlyx är genomgående skapat med sökmotoroptimering som en fokuspunkt</p>
</div>
<div class="feature" style="left:304px;top:635px">
  <svg width="26" height="24" viewBox="0 0 26 24"><rect x="2" y="3" width="22" height="15" fill="none" stroke="#111" stroke-width="2"/><path d="M9 22h8M13 18v4M8 14l10-9" stroke="#111" stroke-width="2"/></svg>
  <h3>Designa din webshop</h3>
  <p>Välj bland färdiga utseendemallar eller skapa din egen grafiska profil med ett par klick.</p>
</div>
<div class="feature" style="left:509px;top:635px">
  <svg width="28" height="24" viewBox="0 0 28 24"><circle cx="9" cy="10" r="5" fill="none" stroke="#111" stroke-width="3.5" stroke-dasharray="2.5 1.5"/><circle cx="20" cy="7" r="4" fill="none" stroke="#111" stroke-width="3" stroke-dasharray="2 1.5"/><circle cx="15" cy="19" r="3" fill="none" stroke="#111" stroke-width="2.5" stroke-dasharray="2 1.2"/></svg>
  <h3>Smart Dashboard</h3>
  <p>På startsidan i din webbutik får du en överblick om senast inkomna ordrar, analys och statistik om försäljningar mm.</p>
</div>

<div class="spec-label" style="top:759px">Tekniska specifikationer</div>
<svg class="arrow" style="left:70px;top:795px" width="10" height="32"><path d="M9 1L1 16l8 15" fill="none" stroke="#ccc"/></svg>
<svg class="arrow" style="left:708px;top:795px" width="10" height="32"><path d="M1 1l8 15-8 15" fill="none" stroke="#ccc"/></svg>
<div class="spec" style="left:95px;top:772px"><h4>Enkel webshop design</h4><p>Det är viktigt att din webbutik har ett utseende och helhetsintryck som stämmer väl överens med din verksamhet / varumärke. Med Vendlyx behövs varken CSS/HTML-kunskaper eller anlita en <span class="more">[...]</span></p></div>
<div class="spec" style="left:248px;top:772px"><h4>Lagerhantering</h4><p>Vendlyx har funktioner för hantera dina varors lagersaldo. Det finns två sätt att arbeta med lagersaldot i Vendlyx. Manuellt lagersaldo: Du kan manuellt sätta lagerstatus på dina varor. Välj att visa <span class="more">[...]</span></p></div>
<div class="spec" style="left:402px;top:772px"><h4>Sökmotoroptimerad (SEO)</h4><p>En väl sökmotoroptimerad webbshop är idag ett måste för att få in nya kunder från sökmotorer. Vendlyx tar sökmotoroptimering på allvar. Webshopen är från grunden skapad med just <span class="more">[...]</span></p></div>
<div class="spec" style="left:555px;top:772px"><h4>Skapa egna betalsätt</h4><p>Vendlyx låter dig hantera din butiks betalsätt. Skapa nya betalningslösningar såsom postförskott, mot faktura, kortbetalning etc.</p></div>

<div class="spec-label" style="top:867px">Affärer och marknadsföring</div>
<svg class="arrow" style="left:70px;top:903px" width="10" height="32"><path d="M9 1L1 16l8 15" fill="none" stroke="#ccc"/></svg>
<svg class="arrow" style="left:708px;top:903px" width="10" height="32"><path d="M1 1l8 15-8 15" fill="none" stroke="#ccc"/></svg>
<div class="spec" style="left:95px;top:880px"><h4>Orderhantering</h4><p>Vendlyx ger dig ett enkelt grafiskt gränssnitt för att hantera dina kunders ordrar. När en kund lagt en order kommer du per automatik få en notifiering via email om detta. Du kan lätt sortera ordrar eller <span class="more">[...]</span></p></div>
<div class="spec" style="left:248px;top:880px"><h4>Inbyggt analysverktyg</h4><p>Vendlyx har ett inbyggt analysverktyg som gör att det är lätt att få översikt över dina besökare och försäljning. Analysverktyget visar med en graf hur många besökare din webshop haft samt antalet <span class="more">[...]</span></p></div>
<div class="spec" style="left:402px;top:880px"><h4>Automatgenererade</h4><p>Sitemaps är en "karta" över alla sidor på en webbplats som gör det enklare hitta. Vendlyx genererar helt automatiskt dessa SiteMaps så att du som webshopsägare slipper göra det manuellt. Det finns två <span class="more">[...]</span></p></div>
<div class="spec" style="left:555px;top:880px"><h4>Social delningsfunktion</h4><p>Att få sina produktsidor länkade från andra websidor är viktigt både för att få fler besökare till webbshoppen samt att få bättre ranking i sökmotorer. Med Vendlyx får du en social delningsfunktion som gör det lätt <span class="more">[...]</span></p></div>

<div class="cta-row">
  <a class="btn btn-primary">&gt;&nbsp; Skapa en webshop</a>
  <a class="btn btn-outline">&gt;&nbsp; Visa fler funktioner</a>
</div>

<div class="contact-band">
  <span><i class="ico"></i>Feedback</span>
  <span><i class="ico"></i>Webform</span>
  <span><i class="ico"></i>info@vendlyx.example</span>
  <span><i class="dot" style="color:#2aa3ef"></i>Vendlyx på Chirpnet</span>
</div>
<footer class="footer">
  <nav><a>Home</a><i>|</i><a>Visa fler funktioner</a><i>|</i><a>Certavo</a><i>|</i><a>Support</a><i>|</i><a>Dokumentation</a></nav>
  <small>©2016 vendlyx. All rights reserved.</small>
</footer>
</body>
</html>
```